Brellwick Finance Stationary Design

We have selected a logo as our winner, we now need a full stationary set to be in the same theme.
Required:
- Letter Head
- Business Card Template
- Custom Envelopes
- A5 Notepad Design (Front cover and content pages. Content pages blank(no lines) but with our branding on them,)
- With Compliments Slip
Updates

Hey All,

We have changed the colour scheme of our logo. Our apologies if anyone has begun designing based off the old scheme. Please see the updated scheme in the brief,

Tobin

Target Market(s)

Target market is experienced property developers and financial institutions.

Industry/Entity Type

Commercial Finance

Font styles to use
Serif

Colors
0054AA
0677BA
7BADD7
CADEEF
E8F1F8
0094D4
00A9DD
6FCCEA
C7EBF8
E9F6FB
00AB8E
00BBA5
67D7C9
C6EFE9
E9F9F6
59FF00
82FF00
B8FF75
E3FFCB
F4FFEA

```html
<!DOCTYPE html>
<html lang="en">
<head>
<meta charset="utf-8">
<title>Brellwick Finance Stationery Set</title>
<link href="https://fonts.googleapis.com/css2?family=Tinos:wght@400;700&display=swap" rel="stylesheet">
<style>
  :root {
    --brand-blue: #0054AA;
    --brand-teal: #00AB8E;
    --paper: #FFFFFF;
    --tint: #E8F1F8;
    --ink: #111111;
    --rule: #C4C4C4;
    --backdrop: #F2F2F2;
  }
  * { box-sizing: border-box; margin: 0; padding: 0; }
  html, body { width: 1200px; height: 996px; overflow: hidden; }
  body {
    position: relative;
    background: var(--backdrop);
    font-family: "Tinos", "Times New Roman", serif;
    color: var(--ink);
  }
  .piece { position: absolute; }

  /* brand name lockup */
  .brand {
    display: flex; align-items: center; gap: 6px;
    color: var(--brand-blue); font-weight: 700;
    letter-spacing: 0.02em; white-space: nowrap; line-height: 1;
  }
  .brand-mark { background: var(--brand-teal); flex: none; }

  .contact-line { display: flex; align-items: center; gap: 4px; font-weight: 700; line-height: 1.4; white-space: nowrap; }
  .contact-line svg { flex: none; fill: var(--ink); }

  /* letterhead */
  .letterhead {
    left: 23px; top: 40px; width: 633px; height: 896px;
    background: var(--paper); border: 10px solid var(--brand-blue);
  }
  .letterhead-header { position: absolute; left: 0; right: 0; top: 0; height: 86px; border-bottom: 4px solid var(--rule); }
  .letterhead-header .brand { position: absolute; left: 20px; top: 29px; font-size: 20px; }
  .letterhead-header .brand-mark { width: 16px; height: 16px; }
  .sender { position: absolute; left: 382px; top: 14px; font-size: 7px; }
  .sender-name { font-size: 12px; font-weight: 700; margin-bottom: 2px; line-height: 1.2; }
  .sender-role { font-weight: 700; margin-bottom: 1px; line-height: 1.4; }

  /* framed items */
  .framed { border: 9px solid var(--brand-blue); }
  .framed-inner { width: 100%; height: 100%; border: 5px solid var(--brand-teal); background: var(--tint); position: relative; }

  .card-front { left: 56px; top: 161px; width: 270px; height: 153px; }
  .card-front .brand { position: absolute; inset: 0; justify-content: center; font-size: 18px; }
  .card-front .brand-mark { width: 14px; height: 14px; }

  .card-back { left: 340px; top: 161px; width: 269px; height: 153px; font-size: 6.5px; }
  .card-back .brand { position: absolute; left: 9px; top: 10px; font-size: 10px; }
  .card-back .brand-mark { width: 9px; height: 9px; }
  .card-name { position: absolute; left: 78px; top: 58px; font-size: 11px; font-weight: 700; }
  .card-name .first { color: var(--brand-blue); }
  .card-name .last { color: var(--brand-teal); }
  .card-role { position: absolute; left: 78px; top: 72px; font-weight: 700; }
  .card-contacts { position: absolute; left: 9px; top: 94px; }
  .card-row { display: flex; gap: 12px; }

  .envelope { left: 44px; top: 548px; width: 591px; height: 287px; font-size: 6.5px; }
  .envelope .brand { position: absolute; left: 18px; top: 26px; font-size: 20px; }
  .envelope .brand-mark { width: 16px; height: 16px; }
  .envelope-sender { position: absolute; left: 18px; top: 193px; }
  .envelope-sender .sender-name { font-size: 11px; font-weight: 400; margin-bottom: 1px; }

  /* notepad */
  .notepad {
    left: 742px; top: 37px; width: 444px; height: 635px;
    background: var(--brand-blue); border-radius: 0 60px 40px 0;
  }
  .spiral { position: absolute; left: -4px; top: 18px; width: 20px; height: 600px; }
  .notepad-panel {
    position: absolute; left: 46px; top: 89px; width: 349px; height: 486px;
    background: var(--paper); border: 8px solid var(--brand-teal);
  }
  .notepad-panel .brand { position: absolute; inset: 0; justify-content: center; font-size: 24px; }
  .notepad-panel .brand-mark { width: 18px; height: 18px; }
  .notepad-web { position: absolute; left: 0; right: 0; top: 584px; justify-content: center; color: var(--paper); font-size: 10px; }
  .notepad-web svg { fill: var(--paper); }

  /* compliments slip */
  .slip { left: 704px; top: 727px; width: 343px; height: 173px; }
  .slip .framed-inner { background: var(--paper); }
  .slip-title { position: absolute; left: 13px; top: 12px; font-size: 17px; }
  .slip-from { position: absolute; left: 13px; top: 83px; font-size: 9px; font-weight: 700; }
  .slip .brand { position: absolute; left: 13px; top: 110px; font-size: 14px; }
  .slip .brand-mark { width: 11px; height: 11px; }
</style>
</head>
<body>
<svg width="0" height="0" style="position:absolute">
  <defs>
    <symbol id="icon-phone" viewBox="0 0 10 10"><path d="M2 1l2 2-1 1.2c.6 1.2 1.6 2.2 2.8 2.8L7 6l2 2-1.2 1.4C4.5 9 1 5.5.6 2.2z"/></symbol>
    <symbol id="icon-mail" viewBox="0 0 10 10"><path d="M0 2h10v6H0z M0 2l5 3.5L10 2" stroke="#fff" stroke-width=".6"/></symbol>
    <symbol id="icon-pin" viewBox="0 0 10 10"><path d="M5 0a3.5 3.5 0 0 1 3.5 3.5C8.5 6 5 10 5 10S1.5 6 1.5 3.5A3.5 3.5 0 0 1 5 0zm0 2a1.4 1.4 0 1 0 0 2.8A1.4 1.4 0 0 0 5 2z"/></symbol>
  </defs>
</svg>

<section class="piece letterhead">
  <header class="letterhead-header">
    <div class="brand"><span class="brand-mark"></span>BRELLWICK FINANCE</div>
    <div class="sender">
      <p class="sender-name">First Last name</p>
      <p class="sender-role">Founder</p>
      <p class="contact-line"><svg width="6" height="6"><use href="#icon-phone"/></svg>+1 123-456-7890</p>
      <p class="contact-line"><svg width="6" height="6"><use href="#icon-mail"/></svg>www.brellwick.com</p>
      <p class="contact-line"><svg width="6" height="6"><use href="#icon-pin"/></svg>your office address will goes here</p>
    </div>
  </header>
</section>

<section class="piece framed card-front">
  <div class="framed-inner"><div class="brand"><span class="brand-mark"></span>BRELLWICK FINANCE</div></div>
</section>

<section class="piece framed card-back">
  <div class="framed-inner">
    <div class="brand"><span class="brand-mark"></span>BRELLWICK FINANCE</div>
    <p class="card-name"><span class="first">First</span> <span class="last">Last name</span></p>
    <p class="card-role">Founder</p>
    <div class="card-contacts">
      <p class="contact-line"><svg width="6" height="6"><use href="#icon-phone"/></svg>+1 123-456-7890</p>
      <div class="card-row">
        <p class="contact-line"><svg width="6" height="6"><use href="#icon-mail"/></svg>www.brellwick.com</p>
        <p class="contact-line"><svg width="6" height="6"><use href="#icon-pin"/></svg>your office address will goes here</p>
      </div>
    </div>
  </div>
</section>

<section class="piece framed envelope">
  <div class="framed-inner">
    <div class="brand"><span class="brand-mark"></span>BRELLWICK FINANCE</div>
    <div class="envelope-sender">
      <p class="sender-name">First Last name</p>
      <p class="sender-role">Founder</p>
      <p class="contact-line"><svg width="6" height="6"><use href="#icon-phone"/></svg>+1 123-456-7890</p>
      <p class="contact-line"><svg width="6" height="6"><use href="#icon-mail"/></svg>www.brellwick.com</p>
      <p class="contact-line"><svg width="6" height="6"><use href="#icon-pin"/></svg>your office address will goes here</p>
    </div>
  </div>
</section>

<section class="piece notepad">
  <svg class="spiral" viewBox="0 0 20 600" aria-hidden="true">
    <g fill="none" stroke="#9A9A9A" stroke-width="2.5">
      <path d="M2 20h14M2 58h14M2 96h14M2 134h14M2 172h14M2 210h14M2 248h14M2 286h14M2 324h14M2 362h14M2 400h14M2 438h14M2 476h14M2 514h14M2 552h14M2 590h14"/>
    </g>
  </svg>
  <div class="notepad-panel"><div class="brand"><span class="brand-mark"></span>BRELLWICK FINANCE</div></div>
  <p class="notepad-web contact-line"><svg width="8" height="8"><use href="#icon-mail"/></svg>www.brellwick.com</p>
</section>

<section class="piece framed slip">
  <div class="framed-inner">
    <p class="slip-title">With Compliments</p>
    <p class="slip-from">From : -</p>
    <div class="brand"><span class="brand-mark"></span>BRELLWICK FINANCE</div>
  </div>
</section>
</body>
</html>
```